Business Card Design

We would like a business card that utilizes our current logo and keeps with the same feel - elegant and organic. Our farm isn't about mass production, it's about excellence, education, beautiful events and flowers - people, culture, and community.

Target Market(s)

Patrons to our farm who are interested in weddings, events, or our flowers and vegetables.

Contact Information for Business Card

Name, address, cell email (Danielle Hoskins, 2716 Wrenfield Rd, Alderton, CO 80621, cell 30.412.6638, email danielle@wrenfieldacres.com)

```html
<!DOCTYPE html>
<html lang="en">
<head>
<meta charset="utf-8">
<title>Wrenfield Acres — Business Card</title>
<link href="https://fonts.googleapis.com/css2?family=Roboto:wght@400;500;700&display=swap" rel="stylesheet">
<style>
  :root {
    --canvas: #e9e6e1;
    --card-dark: #262626;
    --card-light: #ffffff;
    --tan: #a67f56;
    --sage: #7d917f;
    --silver: #9a9a9a;
    --ink-grey: #4a4a4a;
    --white: #ffffff;
  }
  * { box-sizing: border-box; margin: 0; padding: 0; }
  html, body {
    width: 1200px; height: 900px; overflow: hidden;
    background: var(--canvas);
    font-family: "Roboto", Arial, sans-serif;
  }
  .stage {
    width: 1200px; height: 900px;
    display: flex; flex-direction: column; align-items: center; justify-content: center;
    gap: 34px;
  }
  .card {
    position: relative;
    width: 700px; height: 400px;
    border-radius: 26px;
    overflow: hidden;
    box-shadow: 0 10px 28px rgba(0,0,0,.18);
  }

  /* Back side */
  .card-back { background: var(--card-dark); display: flex; align-items: center; justify-content: center; }
  .card-back .brand-name {
    color: var(--silver);
    font-size: 46px; font-weight: 400; letter-spacing: .04em;
  }

  /* Front side */
  .card-front { background: var(--card-light); }
  .front-panel { position: absolute; inset: 0; width: 100%; height: 100%; }
  .corner-tab {
    position: absolute; top: 28px; right: 0;
    width: 16px; height: 22px; background: var(--tan);
  }
  .front-brand {
    position: absolute; left: 48px; top: 150px;
    color: var(--sage);
    font-size: 30px; font-weight: 400; letter-spacing: .03em;
  }
  .identity {
    position: absolute; right: 42px; top: 44px; text-align: right;
  }
  .identity .person-name {
    color: var(--tan); font-size: 30px; font-weight: 700; letter-spacing: .01em;
    text-transform: uppercase;
  }
  .identity .person-role {
    color: var(--ink-grey); font-size: 20px; font-weight: 400; margin-top: 2px;
  }
  .contact {
    position: absolute; right: 40px; bottom: 48px;
    list-style: none; text-align: right;
    color: var(--white); font-size: 20px; line-height: 1.3; font-weight: 400;
  }
  .contact li { display: flex; justify-content: flex-end; align-items: center; gap: 6px; }
  .contact svg { width: 16px; height: 16px; flex: none; }
</style>
</head>
<body>
<main class="stage">

  <section class="card card-back" aria-label="Business card, back">
    <span class="brand-name">Wrenfield Acres</span>
  </section>

  <section class="card card-front" aria-label="Business card, front">
    <svg class="front-panel" viewBox="0 0 700 400" preserveAspectRatio="none" aria-hidden="true">
      <path d="M190 400 C 200 300, 300 210, 440 185 C 540 166, 640 160, 700 160 L700 400 Z" fill="var(--tan)"/>
    </svg>
    <svg class="front-panel" viewBox="0 0 700 400" preserveAspectRatio="none" role="img" aria-label="Soft sage leaf sprig decoration sweeping across the card">
      <path d="M330 175 C 430 140, 560 112, 680 110 C 630 130, 540 148, 450 160 C 400 167, 360 172, 330 175 Z" fill="var(--sage)" opacity=".35"/>
    </svg>
    <div class="corner-tab" aria-hidden="true"></div>

    <span class="front-brand">Wrenfield Acres</span>

    <div class="identity">
      <p class="person-name">Danielle Hoskins</p>
      <p class="person-role">Director</p>
    </div>

    <ul class="contact">
      <li>2716 Wrenfield Rd,</li>
      <li>Alderton, CO 80621</li>
      <li>30.412.6638
        <svg viewBox="0 0 24 24" aria-hidden="true"><path fill="currentColor" d="M6.6 10.8a15 15 0 0 0 6.6 6.6l2.2-2.2c.3-.3.7-.4 1-.2 1.1.4 2.3.6 3.6.6.6 0 1 .4 1 1V20c0 .6-.4 1-1 1C10.6 21 3 13.4 3 4c0-.6.4-1 1-1h3.5c.6 0 1 .4 1 1 0 1.3.2 2.5.6 3.6.1.3 0 .7-.2 1z"/></svg>
      </li>
      <li>danielle@wrenfieldacres.com
        <svg viewBox="0 0 24 24" aria-hidden="true"><rect x="3" y="5" width="18" height="14" rx="1.5" fill="none" stroke="currentColor" stroke-width="2"/><path d="M3.5 6l8.5 7 8.5-7" fill="none" stroke="currentColor" stroke-width="2"/></svg>
      </li>
    </ul>
  </section>

</main>
</body>
</html>
```